Brindlewood Print Works Needs a Post Card / Flyer

We are a business equipment company and we sell and lease Quorvan copiers. Due to requests from our customers, we opened a speciality printing service in our facility. (Since we have the same machines that speciality print shops use) We print basically anything that a corporate customer would take to Tallmark Prestos or the Wexby Depot. We are generally 40-50% lower with a faster turn around. Perfect bound, spiral bound manuals, booklets, presentations, catalogs, flyers, etc. If you are needing a quick print job for your company and you are thinking of taking it to Tallmark Prestos or the Wexby Depot, you will save a lot of money calling us first.
We need a simple but eye catching post card and matching flyer. The value proposition is simple: 40-50% less then Tallmark or Wexby and a quicker turn around with free delivery. Eliminate the middle man!
Our website is www.BrindlewoodPrintWorks.example and our phone # is 704-555-0193. We will add a page to the site that matches the winning deisgn
Corporate customers
Printing

```html
<!DOCTYPE html>
<html lang="en">
<head>
<meta charset="utf-8">
<title>Brindlewood Print Works — Flyer</title>
<link rel="stylesheet" href="https://fonts.googleapis.com/css2?family=Montserrat:wght@600;700&family=Questrial&display=swap">
<style>
  :root {
    --paper: #f4f4f3;
    --blue-deep: #1c3a9a;
    --blue-light: #2f73d2;
    --slate: #5c6d72;
    --orange: #f08a12;
    --orange-dark: #d86d05;
    --navy: #1f2f8a;
    --white: #ffffff;
  }
  * { margin: 0; padding: 0; box-sizing: border-box; }
  html, body { width: 1059px; height: 1200px; overflow: hidden; background: var(--paper); }
  .flyer {
    position: relative;
    width: 1059px;
    height: 1200px;
    background: var(--paper);
    font-family: "Questrial", "Century Gothic", sans-serif;
    overflow: hidden;
  }
  .flyer__swoosh { position: absolute; inset: 0; width: 1059px; height: 1200px; }
  .brand {
    position: absolute;
    top: 135px;
    left: 0;
    width: 100%;
    display: flex;
    justify-content: center;
    align-items: center;
    gap: 18px;
  }
  .brand__dot {
    width: 62px; height: 62px; border-radius: 50%;
    background: var(--navy);
  }
  .brand__name {
    font-family: "Montserrat", sans-serif;
    font-weight: 700;
    font-size: 44px;
    color: var(--navy);
    letter-spacing: -0.5px;
  }
  .offer {
    position: absolute;
    top: 420px;
    left: 0;
    width: 100%;
    text-align: center;
  }
  .offer__headline {
    display: flex;
    justify-content: center;
    align-items: center;
    gap: 16px;
    height: 100px;
  }
  .offer__arrow { width: 70px; height: 70px; }
  .offer__percent {
    font-family: "Montserrat", sans-serif;
    font-weight: 700;
    font-size: 84px;
    color: var(--orange);
    -webkit-text-stroke: 3px var(--white);
    paint-order: stroke fill;
    line-height: 1;
  }
  .offer__line {
    color: var(--orange);
    font-size: 48px;
    line-height: 56px;
  }
  .offer__with {
    color: var(--orange);
    font-size: 36px;
    line-height: 54px;
  }
  .offer__free {
    color: var(--white);
    font-size: 58px;
    line-height: 70px;
    margin-top: 4px;
  }
  .offer__tagline {
    color: var(--white);
    font-size: 44px;
    line-height: 56px;
  }
  .contact__web {
    position: absolute;
    top: 1012px;
    left: 0;
    width: 100%;
    text-align: center;
    color: var(--navy);
    font-size: 31px;
  }
  .contact__phone {
    position: absolute;
    top: 1063px;
    left: 312px;
    width: 485px;
    height: 84px;
    border-radius: 14px;
    background: linear-gradient(180deg, #f7a12e 0%, var(--orange) 50%, var(--orange-dark) 100%);
    display: flex;
    align-items: center;
    justify-content: center;
    gap: 10px;
    color: var(--white);
    font-size: 52px;
  }
  .contact__icon { width: 44px; height: 44px; }
</style>
</head>
<body>
<main class="flyer">
  <svg class="flyer__swoosh" viewBox="0 0 1059 1200" aria-hidden="true">
    <defs>
      <radialGradient id="bandGlow" cx="0.42" cy="0.45" r="0.65">
        <stop offset="0" stop-color="#3a82dc"/>
        <stop offset="0.55" stop-color="#2656b8"/>
        <stop offset="1" stop-color="#1c3a9a"/>
      </radialGradient>
    </defs>
    <path d="M0,120 C260,320 650,370 1059,195" fill="none" stroke="var(--slate)" stroke-width="14"/>
    <path d="M0,160 C250,345 650,395 1059,228 L1059,815 C700,860 300,920 0,1030 Z" fill="url(#bandGlow)"/>
    <path d="M0,1095 C220,985 520,900 950,850" fill="none" stroke="var(--slate)" stroke-width="14"/>
  </svg>

  <header class="brand">
    <span class="brand__dot"></span>
    <span class="brand__name">Brindlewood Print Works</span>
  </header>

  <section class="offer">
    <div class="offer__headline">
      <svg class="offer__arrow" viewBox="0 0 70 70" aria-hidden="true">
        <path d="M8,10 C30,10 40,22 40,40 L40,44 L54,44 L32,68 L10,44 L24,44 L24,40 C24,30 18,26 8,26 Z" fill="var(--orange)" stroke="var(--white)" stroke-width="3"/>
      </svg>
      <span class="offer__percent">40-50%</span>
    </div>
    <p class="offer__line">less then Tallmark or Wexby</p>
    <p class="offer__line">and a quicker turn around</p>
    <p class="offer__with">WITH</p>
    <p class="offer__free">FREE DELIVERY</p>
    <p class="offer__tagline">Eliminate the middle man!</p>
  </section>

  <p class="contact__web">www.BrindlewoodPrintWorks.example</p>
  <div class="contact__phone">
    <svg class="contact__icon" viewBox="0 0 24 24" aria-hidden="true">
      <path d="M6.6 10.8c1.4 2.8 3.8 5.1 6.6 6.6l2.2-2.2c.3-.3.7-.4 1-.2 1.1.4 2.3.6 3.6.6.6 0 1 .4 1 1V20c0 .6-.4 1-1 1C10.6 21 3 13.4 3 4c0-.6.4-1 1-1h3.5c.6 0 1 .4 1 1 0 1.3.2 2.5.6 3.6.1.3 0 .7-.2 1l-2.3 2.2z" fill="var(--navy)"/>
    </svg>
    <span class="contact__number">704-555-0193</span>
  </div>
</main>
</body>
</html>
```